Clever & creative business card needed for a pediatric dentist.

We need a business card for a pediatric dentist that is building a brand-new pediatric dental practice. He is funny, outgoing, and sociable, and he hopes to give his business card to dentists and pediatricians so that he can give them information of where to refer infants, children, and teenagers that need high quality and attainable dental care.

The name of the dental practice is Copper Fern Pediatric Dentistry. Logo design .png / .pdf/ .jpg are provided to aid in the design.

The dentist's last name is Tolvan (which sounds like "burger", as in "hamburger” or “cheeseburger"). Since it is pediatric practice, kudos will be given to designs that implement a little joke into the design - but hopefully in a small or hidden way (such as putting something like a cheeseburger on the back of the card, or hiding it an an abstract way).

Thank you!

Please make a design that incorporates colors. It should be fun! Not too serious. It does not have to follow the color scheme of the logos.

```html
<!DOCTYPE html>
<html lang="en">
<head>
<meta charset="utf-8">
<title>Copper Fern Pediatric Dentistry – Business Card</title>
<link rel="stylesheet" href="https://fonts.googleapis.com/css2?family=Open+Sans:wght@400;600;700&family=Varela+Round&display=swap">
<style>
  :root {
    --canvas-bg: #ecebe8;
    --front-top: #8f9192;
    --front-bottom: #5f6263;
    --front-ink: #f3f4f4;
    --front-ink-soft: #d9dbdc;
    --back-paper: #f7f8f7;
    --back-edge: #e6e9e7;
    --ink-dark: #3a3d3f;
    --ink-mid: #4d5254;
    --brand-green: #3fa35c;
    --brand-green-soft: #dcece0;
  }
  * { box-sizing: border-box; margin: 0; padding: 0; }
  html, body {
    width: 1200px; height: 1023px; overflow: hidden;
    background: var(--canvas-bg);
  }
  .canvas {
    position: relative; width: 1200px; height: 1023px;
  }
  .card {
    position: absolute; width: 540px; height: 309px;
    border-radius: 4px;
    box-shadow: 0 10px 28px rgba(0,0,0,0.18);
    overflow: hidden;
  }

  /* Front */
  .card-front {
    left: 70px; top: 120px;
    background: linear-gradient(160deg, var(--front-top), var(--front-bottom));
    display: flex; align-items: center; justify-content: center;
  }
  .front-brand { text-align: center; }
  .front-brand .brand-name {
    font-family: 'Varela Round', sans-serif;
    font-size: 58px; line-height: 1; letter-spacing: 1px;
    color: var(--front-ink);
  }
  .front-brand .brand-tagline {
    margin-top: 10px;
    font-family: 'Open Sans', sans-serif; font-weight: 400;
    font-size: 15px; letter-spacing: 6px;
    color: var(--front-ink-soft);
  }

  /* Back */
  .card-back {
    left: 590px; top: 594px;
    background: var(--back-paper);
    border: 1px solid var(--back-edge);
  }
  .back-watermark {
    position: absolute; left: 150px; top: -40px;
    width: 300px; height: 300px;
  }
  .contact {
    position: absolute; left: 30px; top: 30px;
    font-family: 'Open Sans', sans-serif; color: var(--ink-mid);
    font-size: 13px; line-height: 1.45;
  }
  .contact .person-name {
    font-weight: 700; font-size: 19px; color: var(--ink-dark);
  }
  .contact .person-role {
    color: var(--brand-green); font-size: 13px; margin-bottom: 6px;
  }
  .back-brand {
    position: absolute; right: 30px; top: 168px;
    display: flex; align-items: center; gap: 12px;
  }
  .back-brand .brand-mark {
    width: 34px; height: 34px; border-radius: 4px;
    background: var(--brand-green);
  }
  .back-brand .brand-name {
    font-family: 'Varela Round', sans-serif;
    font-size: 34px; line-height: 1; color: var(--ink-dark);
  }
  .back-brand .brand-tagline {
    font-family: 'Open Sans', sans-serif;
    font-size: 10px; letter-spacing: 4px; color: var(--ink-mid);
    margin-top: 5px;
  }
  .address {
    position: absolute; right: 30px; bottom: 24px; text-align: right;
    font-family: 'Open Sans', sans-serif; font-size: 12px;
    line-height: 1.45; color: var(--ink-mid);
  }
</style>
</head>
<body>
  <main class="canvas">
    <section class="card card-front" aria-label="Card front">
      <div class="front-brand">
        <div class="brand-name">copper fern</div>
        <div class="brand-tagline">PEDIATRIC DENTISTRY</div>
      </div>
    </section>

    <section class="card card-back" aria-label="Card back">
      <svg class="back-watermark" viewBox="0 0 300 300" aria-hidden="true">
        <circle cx="150" cy="150" r="140" fill="var(--brand-green-soft)" opacity="0.7"/>
      </svg>

      <div class="contact">
        <div class="person-name">Your Name Here</div>
        <div class="person-role">Managing Director</div>
        <div>(555) 014-2290</div>
        <div>(555) 014-2290</div>
        <div>youremail@youremail.com</div>
        <div>yourwebsite.com</div>
      </div>

      <div class="back-brand">
        <div>
          <div class="brand-name">copper fern</div>
          <div class="brand-tagline">PEDIATRIC DENTISTRY</div>
        </div>
        <div class="brand-mark"></div>
      </div>

      <div class="address">
        418 Larkspur Way,<br>
        #12 Fernhill, Nevada 89000
      </div>
    </section>
  </main>
</body>
</html>
```